Pellham Ridge Nectar Company, local Honey producer needs product Lable to encourage sales

We are a small business (Pellham Ridge Nectar Company) located in a small Texas town that harvests honey from our beehives yearly. Our honey would be considered "raw wildflower honey" and our goal is to sell it locally (farmers markets) and to surrounding areas.

We are currently packaging in plastic classic honey bottles with white flip caps. Sizes are 8oz and 16oz bottles (see pictures for actual size). Larger orders will be filled in one quart mason jars.

Design Ideas:
-vintage style design with bee or several bees in background
- incorporate company name "Pellham Ridge Nectar Company"
- needs small description "Raw Honey", and "Harvested in Calloway Springs, Texas"

Target Market(s)

Farmers markets, health conscience people looking for unprocessed food options

Industry/Entity Type

Small Business

Requirements
Nice to have
• Vintage feel
Should not have
• No cartoonish characters

```html
<!DOCTYPE html>
<html lang="en">
<head>
<meta charset="utf-8">
<title>Pellham Ridge Nectar Company – Raw Honey Label</title>
<link rel="stylesheet" href="https://fonts.googleapis.com/css2?family=Federo&family=Josefin+Sans:wght@300;400&display=swap">
<style>
  :root {
    --page: #f3f0eb;
    --label-cream: #f8ebcf;
    --ink-brown: #7d5c45;
    --ink-brown-soft: rgba(125, 92, 69, 0.55);
    --comb-dark: #2f2f2f;
    --comb-mid: #6b6b66;
    --bee-dark: #2b3a35;
    --bee-red: #9a3b2e;
    --bee-wing: #8f8a5e;
  }
  html, body {
    margin: 0;
    padding: 0;
    width: 1200px;
    height: 1000px;
    overflow: hidden;
    background: var(--page);
  }
  .canvas {
    position: relative;
    width: 1200px;
    height: 1000px;
  }
  .honey-label {
    position: absolute;
    left: 330px;
    top: 50px;
    width: 540px;
    height: 900px;
    border-radius: 270px;
    background: var(--label-cream);
    overflow: hidden;
    box-shadow: 0 0 0 1px rgba(125, 92, 69, 0.12);
  }
  .ornament {
    position: absolute;
    left: 90px;
    width: 360px;
    border-radius: 60px;
    background: radial-gradient(ellipse at center, var(--ink-brown-soft) 0%, rgba(125, 92, 69, 0.25) 60%, rgba(125, 92, 69, 0) 100%);
  }
  .ornament--top { top: 34px; height: 118px; }
  .ornament--bottom { top: 742px; height: 120px; }
  .divider {
    position: absolute;
    left: 80px;
    width: 380px;
    height: 2px;
    background: var(--ink-brown);
  }
  .divider--top { top: 160px; }
  .divider--bottom { top: 730px; }
  .brand-name {
    position: absolute;
    top: 178px;
    left: 0;
    width: 100%;
    margin: 0;
    text-align: center;
    font-family: "Federo", sans-serif;
    font-weight: 400;
    font-size: 41px;
    line-height: 46px;
    color: var(--ink-brown);
    letter-spacing: 0.5px;
  }
  .honeycomb {
    position: absolute;
    background: linear-gradient(160deg, var(--comb-mid) 0%, var(--comb-dark) 55%, var(--comb-mid) 100%);
    border-radius: 40px;
  }
  .honeycomb--left { left: -20px; top: 363px; width: 170px; height: 300px; }
  .honeycomb--right { left: 390px; top: 280px; width: 170px; height: 306px; }
  .bee {
    position: absolute;
    left: 155px;
    top: 330px;
    width: 220px;
    height: 235px;
    border-radius: 45%;
    background: radial-gradient(ellipse at 50% 35%, var(--bee-red) 0%, var(--bee-dark) 35%, var(--bee-wing) 70%, rgba(143, 138, 94, 0) 100%);
  }
  .product-info {
    position: absolute;
    z-index: 2;
    top: 612px;
    left: 0;
    width: 100%;
    text-align: center;
    color: var(--ink-brown);
    font-family: "Josefin Sans", sans-serif;
    font-weight: 300;
  }
  .product-info .net-weight {
    font-family: "Federo", sans-serif;
    font-size: 30px;
    line-height: 36px;
  }
  .product-info .net-weight small { font-size: 14px; }
  .product-info .product-type {
    font-size: 24px;
    line-height: 34px;
    letter-spacing: 0.5px;
  }
  .product-info .origin {
    font-size: 19px;
    line-height: 28px;
  }
</style>
</head>
<body>
<main class="canvas">
  <section class="honey-label">
    <div class="ornament ornament--top" role="img" aria-label="Vintage scrollwork flourish ornament"></div>
    <div class="divider divider--top"></div>

    <h1 class="brand-name">Pellham Ridge<br>Nectar Company</h1>

    <div class="honeycomb honeycomb--left" role="img" aria-label="Engraved vintage honeycomb illustration"></div>
    <div class="honeycomb honeycomb--right" role="img" aria-label="Engraved vintage honeycomb illustration"></div>
    <div class="bee" role="img" aria-label="Vintage engraved bumblebee illustration"></div>

    <div class="product-info">
      <div class="net-weight">8<small>oz</small></div>
      <div class="product-type">RAW HONEY.</div>
      <div class="origin">Harvested in Calloway Springs, Texas.</div>
    </div>

    <div class="divider divider--bottom"></div>
    <div class="ornament ornament--bottom" role="img" aria-label="Vintage scrollwork flourish ornament"></div>
  </section>
</main>
</body>
</html>
```